Design required for boutique fire engineering firm in New Zealand

Our website was published based on free Wordpress templates, we'd like something a bit more bespoke, clean and simple.
Updates

Reason: didn't check this finished on a Sunday :)

Target Market(s)

architects, building owners, property developers

Industry/Entity Type

Boutique

Contact Information for Business Card

Logo
Fire Engineering

Desmond Harlow
Principal
+64 21 482 735
desmond@veltrane.nz
veltrane.nz

Number of Pages Required

3 page

Font styles to use
Sans Serif

Requirements
Nice to have
• On the business card, an embossed logo would be great - not sure if that's a design thing or just a print thing?
• Website, existing @ http://veltrane.nz for extent of content and general arrangement that I'm happy with.
• Ability to update the content with project bio's and some photos at a later date would be nice.

```html
<!DOCTYPE html>
<html lang="en">
<head>
<meta charset="utf-8">
<title>Veltrane – Fire Engineering</title>
<link href="https://fonts.googleapis.com/css2?family=PT+Sans:wght@400;700&display=swap" rel="stylesheet">
<style>
  :root {
    --navy: #033a5a;
    --navy-text: #0a3c5c;
    --body-text: #3f6d8e;
    --nav-text: #1f4a68;
    --white: #ffffff;
    --hero-top: #8fa6b4;
    --hero-mid: #4f6d98;
    --hero-bottom: #3c5c8c;
    --photo-grey: #a9a9a9;
  }
  * { box-sizing: border-box; margin: 0; padding: 0; }
  html, body { width: 1200px; height: 883px; overflow: hidden; background: var(--white); }
  body { font-family: "PT Sans", sans-serif; position: relative; }

  .site-header {
    position: absolute; left: 0; top: 0; width: 1200px; height: 65px;
    background: var(--white); display: flex; align-items: center;
    box-shadow: 0 1px 3px rgba(0,0,0,0.08); z-index: 2;
  }
  .brand { position: absolute; left: 92px; top: 10px; display: flex; align-items: center; gap: 8px; }
  .brand-mark { width: 44px; height: 44px; border-radius: 50%; background: var(--navy); }
  .brand-name { font-size: 34px; font-weight: 700; color: var(--navy); letter-spacing: 0.5px; }
  .main-nav { position: absolute; right: 92px; top: 22px; display: flex; gap: 36px; }
  .main-nav a { font-size: 15.5px; color: var(--nav-text); text-decoration: none; letter-spacing: 1px; }

  .hero {
    position: absolute; left: 0; top: 65px; width: 1200px; height: 481px;
    background: linear-gradient(180deg, var(--hero-top) 0%, var(--hero-mid) 30%, var(--hero-bottom) 100%);
  }
  .hero-title {
    position: absolute; left: 87px; top: 157px; font-size: 49px; font-weight: 700;
    color: var(--white); letter-spacing: 3.5px;
  }
  .hero-tagline {
    position: absolute; left: 93px; top: 225px; font-size: 15.5px; color: var(--white); letter-spacing: 1px;
  }
  .hero-button {
    position: absolute; left: 95px; top: 272px; width: 132px; height: 39px; border-radius: 20px;
    background: var(--white); color: var(--navy); font-size: 15.5px; font-weight: 700; letter-spacing: 1px;
    display: flex; align-items: center; justify-content: center; text-decoration: none;
    box-shadow: 0 2px 4px rgba(0,0,0,0.2);
  }
  .social-links { position: absolute; left: 1079px; top: 172px; display: flex; flex-direction: column; gap: 25px; }
  .social-links span { width: 28px; height: 28px; border-radius: 50%; background: var(--white); display: block; }

  .location-band {
    position: absolute; left: 0; top: 546px; width: 1200px; height: 93px; background: var(--navy);
    display: flex; align-items: center; justify-content: center; gap: 22px;
  }
  .location-band p { font-size: 23px; color: var(--white); letter-spacing: 1.6px; }

  .about { position: absolute; left: 0; top: 639px; width: 1200px; height: 244px; }
  .about h2 {
    position: absolute; left: 0; width: 1200px; top: 40px; text-align: center;
    font-size: 27px; font-weight: 700; color: var(--navy-text); letter-spacing: 1.5px;
  }
  .about-intro {
    position: absolute; left: 174px; top: 89px; width: 870px; font-size: 15.5px; line-height: 21.3px;
    color: var(--body-text); letter-spacing: 0.8px;
  }
  .founder-photo {
    position: absolute; left: 197px; top: 210px; width: 118px; height: 118px; border-radius: 50%;
    background: radial-gradient(circle at 50% 40%, #d2d2d2, var(--photo-grey));
  }
  .founder-bio {
    position: absolute; left: 347px; top: 230px; width: 700px; font-size: 15.5px; color: var(--body-text);
    letter-spacing: 0.8px; white-space: nowrap;
  }
</style>
</head>
<body>
  <header class="site-header">
    <div class="brand">
      <span class="brand-mark"></span>
      <span class="brand-name">veltrane</span>
    </div>
    <nav class="main-nav">
      <a href="#">Home</a>
      <a href="#">About</a>
      <a href="#">Our Projects</a>
      <a href="#">Contact us</a>
    </nav>
  </header>

  <section class="hero" role="img" aria-label="Blue-toned photo of a silver pen resting on a fabric notebook">
    <h1 class="hero-title">Fire Engineering</h1>
    <p class="hero-tagline">A Thoughtful and Responsive firm</p>
    <a class="hero-button" href="#">Contact us</a>
    <div class="social-links" aria-label="Social links">
      <span></span><span></span><span></span>
    </div>
  </section>

  <section class="location-band">
    <p>Consulting Fire Engineers based in Wellington, New Zealand</p>
    <svg width="30" height="40" viewBox="0 0 30 40" aria-hidden="true">
      <path d="M15 39 C15 39 2 22 2 14 A13 13 0 0 1 28 14 C28 22 15 39 15 39 Z" fill="#c9ced3"/>
      <circle cx="15" cy="14" r="9" fill="#1f4fa0"/>
    </svg>
  </section>

  <section class="about">
    <h2>About us</h2>
    <p class="about-intro">Veltrane is a boutique fire engineering firm based in Wellington, New Zealand, founded by Desmond Harlow in 2017. We provide consulting services in the built environment, including design and review services to assist in Building Consent applications, advice on property protection matters, observation of construction on site, and regulatory consultation.</p>
    <div class="founder-photo" role="img" aria-label="Portrait photo of the founder"></div>
    <p class="founder-bio">Desmond has worked as a fire engineer in New Zealand for over 20 years, having graduated</p>
  </section>
</body>
</html>
```